Flyer YOga studio

I need a double sided DL flyer (landscape) with my yoga studio details on one side and my timetable on the back.
Updates

It looks like a lot of my info didn't save the orignal brief.

here is some information.

On the front side - Logo to be centred on white background.

Underneath text
$20 for 7 days unlimited yoga/pilates/run group
$99 for 1 month unlimited

also to be included - Location: Upstairs, 17 West Parade Linwood 3187
0428 619354
info@hollowmerrick.com.au
www.hollowmerrick.com.au

ON back side - Timetable only

Requirements
Must have
• Following text should be on front side

the logo
New clients offer: $20 for 7 days of Yoga
$99 - 1 month unlimited

Location: Upstairs, 17 West Parade
Linwood VIC 3187
info@hollowmerrick.com.au/0428 619354

The following text:
Stretch...strength...Run
Any order you like...pick all or one. Only fear holds you back from experiencing any of these. We teach all our classes to what is happening in your body in this moment with an eye for alignment, correct muscle recruitment and breath awareness.

On the back:
Class descriptions:
Yoga: Flowing Vinyasa classes that heat the body through dynamic movements and slowing down for deep hip openers and relaxation.
Pilates: Mat classes for healthy bodies using a systematic sequencing of exercises that works the whole body, developing strength, flexibility and mindfulness.
Run groups: A non competitive session where you set the goals and we help you meet them, whether it getting to the corner and back or your first marathon.

```html
<!DOCTYPE html>
<html lang="en">
<head>
<meta charset="utf-8">
<title>Hollow Merrick Yoga – DL Flyer</title>
<link rel="stylesheet" href="https://fonts.googleapis.com/css2?family=Roboto+Condensed:wght@400;700&family=Roboto:wght@400;700&display=swap">
<style>
  :root{
    --stage:#ece7df;
    --paper:#f6f3ee;
    --paper-warm:#e6d9c2;
    --sand:#cdb48a;
    --ink:#4a4a4a;
    --ink-soft:#7a7874;
    --ink-dark:#3a3a3a;
    --rule:#cfc3ad;
    --cell:#ebe4d8;
    --flourish:#d9ccb6;
    --yellow:#f4e61c;
    --orange:#f8b417;
    --blue:#c3e2ea;
    --purple:#b9a8d6;
    --pink:#de4d9b;
    --green:#8dc542;
    --brand-dot:#f2a81d;
  }
  *{box-sizing:border-box;margin:0;padding:0}
  html,body{width:1200px;height:846px;overflow:hidden;background:var(--stage)}
  body{position:relative;font-family:"Roboto",Arial,sans-serif;color:var(--ink)}

  .sheet{position:absolute;overflow:hidden;
    background:linear-gradient(180deg,var(--paper) 0%,var(--paper) 55%,var(--paper-warm) 100%)}
  .sheet--front{left:49px;top:147px;width:529px;height:251px}
  .sheet--timetable{left:49px;top:454px;width:529px;height:251px;background:linear-gradient(180deg,var(--paper),var(--paper-warm))}
  .sheet--flyer{left:621px;top:53px;width:531px;height:750px}
  .swoosh{position:absolute;left:0;width:100%;pointer-events:none}

  .blurb{position:absolute;font-size:8.4px;line-height:1.55;color:var(--ink-soft)}

  .brand{position:absolute;display:flex;align-items:center;gap:10px;justify-content:center}
  .brand__dot{border-radius:50%;background:var(--brand-dot);flex:none}
  .brand__name{font-family:"Roboto Condensed",Arial,sans-serif;font-weight:700;color:var(--ink);
    text-transform:uppercase;white-space:nowrap}

  .flourish{position:absolute;height:9px;border-radius:5px;background:var(--flourish)}

  .offer{position:absolute}
  .offer__title{font-family:"Roboto Condensed",Arial,sans-serif;font-weight:700;font-size:11px;color:var(--ink-dark);text-align:center;text-transform:uppercase;padding-bottom:5px;border-top:1px solid var(--rule);padding-top:4px}
  .offer__box{border:1px solid #a9a39a;border-radius:8px;display:grid;grid-template-columns:38px 1fr}
  .offer__price{font-family:"Roboto Condensed",Arial,sans-serif;font-weight:700;font-size:14px;display:flex;align-items:center;justify-content:center;border-right:1px dashed #a9a39a;color:var(--ink-dark)}
  .offer__text{font-size:8.4px;line-height:1.25;text-align:center;display:flex;align-items:center;justify-content:center;padding:3px}
  .offer__price.first,.offer__text.first{border-bottom:1px dashed #a9a39a}

  .contact{position:absolute;font-family:"Roboto Condensed",Arial,sans-serif;font-size:9.6px;line-height:1.3;color:var(--ink)}
  .contact__label{font-weight:700;font-size:11px;color:var(--ink-dark)}
  .contact--right{text-align:right}
  .contact__phone{font-weight:700;font-size:10.5px;color:var(--ink-dark)}
  .contact__phone small{font-weight:400;font-size:9px}
  .contact__web{font-weight:700;font-size:13px;color:var(--ink-dark)}

  .heading{font-family:"Roboto Condensed",Arial,sans-serif;font-weight:700;color:var(--ink-dark);text-transform:uppercase}
  .descriptions{position:absolute;left:26px;top:284px;width:215px}
  .descriptions .heading--section{font-size:13px;text-align:center;margin-bottom:12px}
  .class{margin-bottom:9px}
  .class__name{font-size:11px;margin-bottom:1px}
  .class__text{font-size:8.4px;line-height:1.3;color:var(--ink-soft)}
  .aside{position:absolute;text-align:left}
  .aside__title{font-size:11px;line-height:1.15;margin-bottom:3px}
  .aside__text{font-size:8px;line-height:1.3;color:var(--ink-soft)}

  .timetable{position:absolute;display:grid;grid-template-columns:52px repeat(7,1fr);
    border:1px solid var(--rule);border-radius:8px;overflow:hidden;background:var(--cell)}
  .timetable > div{border-right:1px solid #d3c8b5;border-bottom:1px solid #d3c8b5;font-size:8.2px;line-height:1.05;
    display:flex;align-items:center;justify-content:center;text-align:center;color:var(--ink-dark)}
  .timetable .day{font-family:"Roboto Condensed",Arial,sans-serif;font-weight:700;font-size:9.5px;background:#f7f4ef}
  .timetable .time{font-family:"Roboto Condensed",Arial,sans-serif;font-weight:700;font-size:9px}
  .timetable .corner{background:#f7f4ef}
  .c-yellow{background:var(--yellow)}.c-orange{background:var(--orange)}.c-blue{background:var(--blue)}
  .c-purple{background:var(--purple)}.c-pink{background:var(--pink)}.c-green{background:var(--green)}
  .timetable--card{left:14px;top:12px;width:501px;height:228px;grid-template-rows:repeat(10,1fr)}
  .timetable--flyer{left:14px;top:514px;width:503px;height:228px;grid-template-rows:repeat(10,1fr)}
</style>
</head>
<body>

<section class="sheet sheet--front">
  <svg class="swoosh" style="top:150px;height:101px" viewBox="0 0 529 101" preserveAspectRatio="none" aria-hidden="true">
    <path d="M0 40 C140 10 330 0 529 30 L529 101 L0 101 Z" fill="#e2d2b6"/>
    <path d="M0 60 C160 35 340 30 529 50 L529 101 L0 101 Z" fill="#d4bd95"/>
  </svg>
  <p class="blurb" style="left:12px;top:12px;width:140px">Stretch...strength...Run<br>Any order you like...pick all or one. Only fear holds you back from experiencing any of these. We teach all our classes to what is happening in your body in this moment with an eye for alignment, correct muscle recruitment and breath awareness.</p>
  <div class="brand" style="left:120px;top:130px;width:260px">
    <span class="brand__dot" style="width:22px;height:22px"></span>
    <span class="brand__name" style="font-size:22px">Hollow Merrick Yoga</span>
  </div>
  <div class="flourish" role="img" aria-label="decorative flourish" style="left:437px;top:22px;width:60px"></div>
  <div class="offer" style="left:388px;top:33px;width:132px">
    <div class="offer__title">New clients offer</div>
    <div class="offer__box">
      <div class="offer__price first" style="height:64px">$20</div>
      <div class="offer__text first">7 days of classes unlimited (yoga, pilates and run group)</div>
      <div class="offer__price" style="height:36px">$99</div>
      <div class="offer__text">1 month unlimited</div>
    </div>
  </div>
  <div class="contact" style="left:14px;top:206px">
    <div class="contact__label">LOCATION:</div>
    Upstairs, 17 West Parade, Linwood, 3187<br>info@hollowmerrick.com.au
  </div>
  <div class="contact contact--right" style="right:14px;top:206px">
    <div class="contact__label">PHONE:</div>
    <div class="contact__phone">0428 619354 <small>- Harriet</small></div>
    <div class="contact__web">www.hollowmerrick.com.au</div>
  </div>
</section>

<section class="sheet sheet--timetable">
  <div class="timetable timetable--card">
    <div class="corner"></div><div class="day">Monday</div><div class="day">Tuesday</div><div class="day">Wednesday</div><div class="day">Thursday</div><div class="day">Friday</div><div class="day">Saturday</div><div class="day">Sunday</div>
    <div class="time">6.15 am</div><div></div><div class="c-yellow">Flow (60)</div><div></div><div class="c-blue">Run group</div><div class="c-yellow">Flow (60)</div><div></div><div></div>
    <div class="time">8 am</div><div></div><div></div><div></div><div></div><div></div><div class="c-blue">Run group<br>(7 am)</div><div></div>
    <div class="time">9.30 am</div><div class="c-orange">Flow (75)</div><div class="c-orange">Flow (75)</div><div class="c-orange">Flow (75)</div><div class="c-orange">Flow (75)</div><div class="c-orange">Flow (75)</div><div class="c-orange">Flow (75)</div><div class="c-orange">Flow (75)</div>
    <div class="time">11 am</div><div></div><div></div><div></div><div></div><div class="c-green">Pilates<br>Open (60)</div><div></div><div></div>
    <div class="time">12.15 pm</div><div class="c-purple">Express<br>Pilates</div><div></div><div class="c-purple">Express<br>Flow (45)</div><div></div><div class="c-purple">Express<br>Flow (45)</div><div></div><div></div>
    <div class="time">4 pm</div><div class="c-pink">Kids Yoga</div><div></div><div></div><div></div><div></div><div></div><div></div>
    <div class="time">6 pm</div><div class="c-blue">Run group<br>(6.15 pm)</div><div class="c-green">Pilates<br>Open (60)</div><div class="c-blue">Run group<br>(6.15 pm)</div><div class="c-yellow">Flow (60)</div><div></div><div></div><div></div>
    <div class="time">7.15 pm</div><div></div><div class="c-orange">Flow (75)</div><div class="c-orange">Flow (75)</div><div class="c-green">Pilates<br>Open (60)</div><div></div><div></div><div></div>
    <div class="time">7.30 pm</div><div class="c-orange">Flow (75)</div><div></div><div></div><div></div><div></div><div></div><div></div>
  </div>
</section>

<section class="sheet sheet--flyer">
  <svg class="swoosh" style="top:250px;height:255px" viewBox="0 0 531 255" preserveAspectRatio="none" aria-hidden="true">
    <rect x="0" y="0" width="531" height="255" fill="#ece3d3"/>
    <path d="M380 15 C320 80 330 200 400 245 L531 245 L531 15 Z" fill="#f3eee6"/>
  </svg>
  <div class="brand" style="left:90px;top:145px;width:300px">
    <span class="brand__dot" style="width:26px;height:26px"></span>
    <span class="brand__name" style="font-size:26px">Hollow Merrick Yoga</span>
  </div>
  <p class="blurb" style="left:398px;top:22px;width:125px">Stretch...strength...Run<br>Any order you like...pick all or one. Only fear holds you back from experiencing any of these. We teach all our classes to what is happening in your body in this moment with an eye for alignment, correct muscle recruitment and breath awareness.</p>
  <div class="contact" style="left:14px;top:202px">
    <div class="contact__label">LOCATION:</div>
    Upstairs, 17 West Parade, Linwood, 3187<br>info@hollowmerrick.com.au
  </div>
  <div class="contact contact--right" style="right:14px;top:202px">
    <div class="contact__label">PHONE:</div>
    <div class="contact__phone">0428 619354 <small>- Harriet</small></div>
    <div class="contact__web">www.hollowmerrick.com.au</div>
  </div>

  <div class="flourish" role="img" aria-label="decorative flourish" style="left:104px;top:270px;width:60px"></div>
  <div class="descriptions">
    <div class="heading heading--section" style="border-bottom:1px solid var(--rule);padding-bottom:3px;margin-left:30px;margin-right:30px">Class descriptions</div>
    <div class="class"><div class="heading class__name">Yoga</div><p class="class__text">Flowing Vinyasa classes that heat the body through dynamic movements and slowing down for deep hip openers and relaxation.</p></div>
    <div class="class"><div class="heading class__name">Pilates</div><p class="class__text">Mat classes for healthy bodies using a systematic sequencing of exercises that works the whole body, developing strength, flexibility and mindfulness.</p></div>
    <div class="class"><div class="heading class__name">Run groups</div><p class="class__text">A non competitive session where you set the goals and we help you meet them, whether it getting to the corner and back or your first marathon.</p></div>
  </div>

  <div class="flourish" role="img" aria-label="decorative flourish" style="left:308px;top:270px;width:56px"></div>
  <div class="offer" style="left:300px;top:287px;width:130px">
    <div class="offer__title">New clients offer</div>
    <div class="offer__box">
      <div class="offer__price first" style="height:52px">$20</div>
      <div class="offer__text first">7 days of classes unlimited (yoga, pilates and run group)</div>
      <div class="offer__price" style="height:32px">$99</div>
      <div class="offer__text">1 month unlimited</div>
    </div>
  </div>

  <div class="brand" style="left:440px;top:325px;width:85px;flex-direction:column;gap:4px">
    <span class="brand__dot" style="width:20px;height:20px"></span>
    <span class="brand__name" style="font-size:10px;white-space:normal;text-align:center;line-height:1.1">Hollow Merrick Yoga</span>
  </div>

  <div class="flourish" role="img" aria-label="decorative flourish" style="left:312px;top:420px;width:50px"></div>
  <div class="aside" style="left:300px;top:436px;width:130px">
    <div class="heading aside__title" style="border-top:1px solid var(--rule);padding-top:4px">Private sessions</div>
    <p class="aside__text">SINGLE OR SMALL GROUPS<br>Available for all disciplines.<br>Just ask.</p>
  </div>
  <div class="flourish" role="img" aria-label="decorative flourish" style="left:455px;top:420px;width:50px"></div>
  <div class="aside" style="left:440px;top:436px;width:85px">
    <div class="heading aside__title" style="border-top:1px solid var(--rule);padding-top:4px">Workshops &amp;<br>short courses</div>
    <p class="aside__text">See website for<br>upcoming events.</p>
  </div>

  <div class="timetable timetable--flyer">
    <div class="corner"></div><div class="day">Monday</div><div class="day">Tuesday</div><div class="day">Wednesday</div><div class="day">Thursday</div><div class="day">Friday</div><div class="day">Saturday</div><div class="day">Sunday</div>
    <div class="time">6.15 am</div><div></div><div class="c-yellow">Flow (60)</div><div></div><div class="c-blue">Run group</div><div class="c-yellow">Flow (60)</div><div></div><div></div>
    <div class="time">8 am</div><div></div><div></div><div></div><div></div><div></div><div class="c-blue">Run group<br>(7 am)</div><div></div>
    <div class="time">9.30 am</div><div class="c-orange">Flow (75)</div><div class="c-orange">Flow (75)</div><div class="c-orange">Flow (75)</div><div class="c-orange">Flow (75)</div><div class="c-orange">Flow (75)</div><div class="c-orange">Flow (75)</div><div class="c-orange">Flow (75)</div>
    <div class="time">11 am</div><div></div><div></div><div></div><div></div><div class="c-green">Pilates<br>Open (60)</div><div></div><div></div>
    <div class="time">12.15 pm</div><div class="c-purple">Express<br>Pilates</div><div></div><div class="c-purple">Express<br>Flow (45)</div><div></div><div class="c-purple">Express<br>Flow (45)</div><div></div><div></div>
    <div class="time">4 pm</div><div class="c-pink">Kids Yoga</div><div></div><div></div><div></div><div></div><div></div><div></div>
    <div class="time">6 pm</div><div class="c-blue">Run group<br>(6.15 pm)</div><div class="c-green">Pilates<br>Open (60)</div><div class="c-blue">Run group<br>(6.15 pm)</div><div class="c-yellow">Flow (60)</div><div></div><div></div><div></div>
    <div class="time">7.15 pm</div><div></div><div class="c-orange">Flow (75)</div><div class="c-orange">Flow (75)</div><div class="c-green">Pilates<br>Open (60)</div><div></div><div></div><div></div>
    <div class="time">7.30 pm</div><div class="c-orange">Flow (75)</div><div></div><div></div><div></div><div></div><div></div><div></div>
  </div>
</section>

</body>
</html>
```